Lens Harbor Teutonia Website - Photography and Films

We are looking for a design that expresses the friendly, open nature of our company Lens Harbor Teutonia, yet at the same time is professional looking and functional.

Lens Harbor Teutonia is a B2B focused operation that hires out multi-lingual camera crews (and equipment) throughout Germany and Europe. We also produce tv features and coporate films. Our unique selling point is that we are native English speakers who can communicate with our international clients (usually British or American) and organise the logistics of shooting in foreign countries.

For content inspiration, see our current website: http://www.lensharborteutonia.com - however we want to move away from the very simple structure of this site and move towards a layout that displays and allows for frequently updated content (e.g. in the form of a blog).

Here is an example of the kind of clean look we like:
http://www.qrvpixelarchive.com/archive/main/reelsqrv.do#reel=48213760

Please keep within the following specifications:
- We wish to keep our logo (grey/white, font: Glypha) and our company colour red (#C40A0A) as they are.
- Maximum Width 960px, on a large browser-window the design should be centred
- Easily readable font sizes with good contrast
- Provide your design in PSD file format
- Our logo should be graphically displayed in the top left of the header.
- The design should allow space for a video.
- The page should have a clearly recognisable end in the form of a footer.

The following menu items need to be clearly arranged so the viewer is not overwhelmed or confused:
About
Services - Crews / Corporate Shoots / Webcasts / Production Arm / Legal Videography
Recent Productions
Blog
Testimonials
Get a Quote
Contact
Film Library
Showreel
Events
Film Location Guide - Frankfurt / Cologne / Zurich / Helsinki / Amsterdam / London / Paris / Rome / Brussels / Berlin / Munich
Updates

Reason: Hi - thanks very much for your interest in our design project.  We are extending this auction because we haven't had enough time to really focus on the desigs and provide immediate feedback to designers.  We will try to provide timely feedback and are giving you more time to make any adjustments to your designs etc.
Thanks!
Marla

Target Market(s)

Our target customers are males and females between 25 and 55 years (mostly British and American). More important than their demographic though, is their occupation - they are largely communication and design savvy individuals belonging to one of the following three categories: 1)Broadcasters (usually producers for example from the QRV or Horizon Vista TV seeking trustworthy, affordable crews for their foreign shoots).

2) Video Production Companies (seeking a trustworthy, affordable partner company to provide the crews for their own corporate clients).

3) Corporate Communications Specialists (seeking professional producers and crews to facilitate production of company videos or filming of events).

Industry/Entity Type

Camera

Requirements
Must have
• A fresh clean appearance with good use of white space.
Should not have
• Avoid dark heavy colours and designs.
• Avoid designs that would be impractical and could potentially take a long time to load.

```html
<!DOCTYPE html>
<html lang="en">
<head>
<meta charset="utf-8">
<title>Lens Harbor Teutonia</title>
<link rel="stylesheet" href="https://fonts.googleapis.com/css2?family=Arvo:wght@700&family=Cabin:wght@600;700&family=Open+Sans:wght@400;600;700&family=Caveat&display=swap">
<style>
:root{
  --red:#c40a0a;
  --red-light:#ef4a4a;
  --ink:#333;
  --grey-text:#777;
  --heading-grey:#8a8a8a;
  --plate-dark:#2d2d2d;
  --plate-mid:#5a5a5a;
  --nav-top:#dcdcdc;
  --nav-bottom:#bcbcbc;
  --panel:#e9e9e9;
  --footer-top:#6e6e6e;
  --footer-bottom:#3c3c3c;
  --teal:#5e9fb4;
}
*{box-sizing:border-box;margin:0;padding:0}
html,body{width:960px;height:1200px;overflow:hidden;background:#fff}
body{font-family:"Open Sans",Arial,sans-serif;color:var(--ink)}
.page{position:relative;width:960px;height:1200px;overflow:hidden;background:var(--panel)}
.abs{position:absolute}

/* header */
.masthead{left:0;top:0;width:960px;height:98px;background:#fff}
.logo-plate{left:22px;top:0;width:585px;height:78px}
.logo-name{left:57px;top:4px;font-family:"Arvo",Georgia,serif;font-weight:700;font-size:41px;color:#fff;letter-spacing:-0.5px}
.contact-plate{left:678px;top:0;width:265px;height:78px}
.contact-mail{left:702px;top:8px;font-size:13px;color:#fff}
.contact-phone{left:702px;top:29px;font-size:24px;color:#fff;letter-spacing:1px}

/* navigation */
.main-nav{left:0;top:98px;width:960px;height:40px;background:linear-gradient(var(--nav-top),var(--nav-bottom));border-top:1px solid #aaa;display:flex;padding-left:40px}
.main-nav a{display:block;height:39px;line-height:39px;padding:0 15px;font-size:13.5px;color:var(--grey-text);text-decoration:none;border-right:1px solid #a9a9a9;border-left:1px solid #e6e6e6}
.main-nav a.current{background:linear-gradient(#f2f2f2,#dedede);color:#444}

/* hero */
.hero-band{left:0;top:138px;width:960px;height:218px;background:linear-gradient(135deg,var(--red-light),#d81c1c 60%,var(--red))}
.hero-floor{left:0;top:356px;width:960px;height:86px;background:linear-gradient(#b9b9b9,#e4e4e4)}
.video-frame{left:78px;top:160px;width:319px;height:259px;background:#fff;border:1px solid #999;box-shadow:0 4px 6px rgba(0,0,0,.35)}
.video-screen{left:0;top:0;width:317px;height:237px;background:#000}
.video-controls{left:0;top:237px;width:317px;height:20px;background:linear-gradient(#f4f4f4,#cfcfcf)}
.hero-title{left:440px;top:160px;font-weight:700;font-size:31px;line-height:35px;color:#fff}
.hero-title .amp{color:#b8b8b8}
.hero-copy{left:440px;top:238px;width:340px;font-size:13.3px;line-height:23.5px;color:#fff}
.quote-btn{left:777px;top:268px;width:148px;height:33px;border-radius:4px;background:linear-gradient(#efefef,#bdbdbd);font-size:20px;color:#666;text-align:center;line-height:33px;box-shadow:0 2px 3px rgba(0,0,0,.3)}
.locations{left:455px;top:334px;width:470px;height:84px;border-radius:5px;background:linear-gradient(#f7f7f7,#cfcfcf);border:1px solid #fff;box-shadow:0 3px 5px rgba(0,0,0,.3)}
.locations-tab{left:3px;top:3px;width:53px;height:76px;background:linear-gradient(90deg,#6eafc3,var(--teal));border-radius:3px 0 0 3px}
.locations-label{left:4px;top:74px;transform:rotate(-90deg);transform-origin:0 0;width:70px;font-weight:700;font-size:15px;line-height:16px;color:#fff}
.thumb{top:7px;height:69px;border:1px solid #888}
.thumb.colosseum{left:103px;width:93px;background:linear-gradient(#5d95d6,#c59a5c 55%,#8a6c40)}
.thumb.beach{left:207px;width:104px;background:linear-gradient(#4f8fd8,#6fa35a 45%,#d6cdb3)}
.thumb.tower{left:321px;width:104px;background:linear-gradient(#1b1da6,#3b3fd0 70%,#c9a23e)}

/* content */
.content-heading{left:42px;top:455px;width:560px;font-family:"Cabin",sans-serif;font-weight:700;font-size:33px;line-height:34px;color:var(--heading-grey)}
.content-copy{left:42px;top:545px;width:560px;font-size:12px;line-height:15px;color:#333}
.content-copy p{margin-bottom:15px}
.content-copy .strong{font-weight:600;font-size:12.5px;letter-spacing:.3px}
.benefits{list-style:none;margin-top:17px}
.benefits li{position:relative;padding-left:20px;margin-bottom:7px}
.benefits li svg{position:absolute;left:0;top:3px}

.tabs{left:31px;top:826px;height:25px;width:400px}
.tab{position:absolute;top:0;height:25px;line-height:27px;font-size:12.5px;letter-spacing:.4px;white-space:nowrap;border-radius:10px 10px 0 0}
.tab.testimonials{left:0;width:140px;padding-left:18px;background:var(--red-light);color:#8a0a0a;z-index:3;clip-path:polygon(0 0,122px 0,140px 25px,0 25px)}
.tab.guide{left:125px;width:142px;padding-left:25px;background:#333;color:#fff;z-index:2;clip-path:polygon(0 0,124px 0,142px 25px,0 25px)}
.tab.contact{left:240px;width:156px;padding-left:47px;background:#777;color:#fff;z-index:1;clip-path:polygon(0 0,138px 0,156px 25px,0 25px)}
.testimonial-panel{left:31px;top:850px;width:586px;height:106px;background:linear-gradient(#d92a2a,var(--red));border:1px solid #9b0707;box-shadow:0 4px 5px rgba(0,0,0,.3)}
.quote-text{left:72px;top:15px;width:450px;font-size:11.5px;line-height:17.5px;color:#fff}
.quote-author{left:345px;top:82px;font-size:11px;color:#fff}
.quote-mark{font-family:Georgia,serif;font-weight:700;font-size:90px;color:#fff;line-height:1}

/* sidebar */
.sidebar-rule{left:630px;top:442px;width:2px;height:548px;background:#cfcfcf;border-right:1px solid #f8f8f8}
.news-heading{left:652px;top:455px;font-family:"Cabin",sans-serif;font-weight:700;font-size:33px;color:var(--heading-grey)}
.post{left:647px;width:300px;height:212px;background:linear-gradient(135deg,#dcdcdc,#f2f2f2 60%,#e0e0e0);border:1px dashed #bbb}
.post-title{left:8px;top:12px;font-size:26px;color:#e02020;letter-spacing:.5px}
.post-meta{left:10px;top:54px;font-size:11.5px;color:#777}
.post-meta a{color:#e02020}
.post-body{left:10px;top:76px;width:265px;font-size:11.5px;line-height:17.5px;color:#333}
.post-more{left:183px;top:166px;font-size:12px;color:#e02020}
.post-comments{left:12px;top:188px;font-size:12px;font-weight:600;color:#777}
.share{left:816px;top:938px;font-family:"Caveat",cursive;font-size:20px;color:#777}
.blog-tab{left:650px;top:963px;width:145px;height:27px;background:#3b3b3b;clip-path:polygon(0 0,125px 0,145px 27px,0 27px);color:#fff;font-size:13px;line-height:29px;padding-left:14px}
.share-dot{top:970px;width:20px;height:20px;border-radius:4px}

/* footer */
.site-footer{left:0;top:990px;width:960px;height:210px;background:linear-gradient(var(--footer-top),var(--footer-bottom));border-top:2px solid #3a3a3a}
.footer-col{top:14px}
.footer-col h3{font-weight:400;font-size:14px;color:#e23a3a;margin-bottom:6px}
.footer-col ul{list-style:none;font-size:12px;line-height:13.5px;color:#fff}
.footer-rule{top:10px;width:1px;height:185px;background:#555;border-right:1px solid #888}
.footer-about{left:673px;top:14px;color:#e6e6e6}
.footer-about .copy{font-size:16px;letter-spacing:.5px;margin-bottom:14px}
.footer-about p{font-size:10.5px;line-height:17.5px}
</style>
</head>
<body>
<div class="page">

  <header class="masthead abs">
    <svg class="logo-plate abs" viewBox="0 0 585 78" width="585" height="78" aria-hidden="true">
      <defs><linearGradient id="plate" x1="0" y1="0" x2="0" y2="1"><stop offset="0" stop-color="#5e5e5e"/><stop offset="1" stop-color="#2b2b2b"/></linearGradient></defs>
      <path d="M2 0H580L548 62Q544 70 534 70H14Q2 70 2 58Z" fill="url(#plate)"/>
      <path d="M10 72H540L548 78H16Z" fill="#ccc"/>
    </svg>
    <div class="logo-name abs">lensharborteutonia</div>
    <svg class="contact-plate abs" viewBox="0 0 265 78" width="265" height="78" aria-hidden="true">
      <path d="M2 0H262L232 62Q228 70 218 70H14Q2 70 2 58Z" fill="url(#plate)"/>
    </svg>
    <div class="contact-mail abs">info@lens-harbor-teutonia.com</div>
    <div class="contact-phone abs">+49-69-417253</div>
  </header>

  <nav class="main-nav abs">
    <a class="current">About</a><a>Services</a><a>Recent Productions</a><a>Film Library</a><a>Showreel</a><a>Events</a><a>Contact Us</a>
  </nav>

  <section class="hero">
    <div class="hero-band abs"></div>
    <div class="hero-floor abs"></div>
    <div class="video-frame abs">
      <div class="video-screen abs" role="img" aria-label="Showreel video player">
        <svg class="abs" style="left:150px;top:112px" width="20" height="20" viewBox="0 0 20 20"><path d="M2 1L19 10L2 19Z" fill="#fff"/></svg>
      </div>
      <div class="video-controls abs">
        <svg width="317" height="20" viewBox="0 0 317 20" aria-hidden="true">
          <path d="M6 6L12 10L6 14Z" fill="#222"/>
          <text x="22" y="14" font-size="8" font-weight="700" fill="#222" font-family="Open Sans,sans-serif">00:01</text>
          <rect x="60" y="8" width="170" height="3" fill="#888"/>
          <text x="234" y="14" font-size="8" font-weight="700" fill="#222" font-family="Open Sans,sans-serif">100 %</text>
          <rect x="278" y="5" width="9" height="9" fill="none" stroke="#222"/>
          <path d="M296 8h3l4-3v10l-4-3h-3Z" fill="#222"/>
        </svg>
      </div>
    </div>
    <h1 class="hero-title abs">Lorem <span class="amp">&amp;</span> ipsum<br>sit amet consectetur</h1>
    <p class="hero-copy abs">Vestibulum eget eros in augue vestibulum imperdiet a at leo. Sed elementum rutrum augue sit amet aliquam. Morbi metus leo, hendrerit at hendrerit nec.</p>
    <div class="quote-btn abs">GET A QUOTE</div>
    <div class="locations abs">
      <div class="locations-tab abs"></div>
      <div class="locations-label abs">Film<br>locations</div>
      <svg class="abs" style="left:80px;top:32px" width="22" height="22" viewBox="0 0 22 22" aria-hidden="true"><circle cx="11" cy="11" r="9.5" fill="#eee" stroke="#999"/><path d="M12 7l-4 4 4 4M16 7l-4 4 4 4" fill="none" stroke="#888" stroke-width="1.6"/></svg>
      <div class="thumb colosseum abs" role="img" aria-label="Film location photo: Rome amphitheatre"></div>
      <div class="thumb beach abs" role="img" aria-label="Film location photo: tropical beach"></div>
      <div class="thumb tower abs" role="img" aria-label="Film location photo: Paris at night"></div>
      <svg class="abs" style="left:444px;top:32px" width="22" height="22" viewBox="0 0 22 22" aria-hidden="true"><circle cx="11" cy="11" r="9.5" fill="#eee" stroke="#999"/><path d="M6 7l4 4-4 4M10 7l4 4-4 4" fill="none" stroke="#888" stroke-width="1.6"/></svg>
    </div>
  </section>

  <main>
    <h2 class="content-heading abs">english speaking camera crews throughout germany and europe</h2>
    <div class="content-copy abs">
      <p>We set up Lens Harbor Teutonia to meet the demands of a growing number of TV-producers whose working language is English. This is our Passion! Why else would we keep doing it for over 30 years!</p>
      <p>As a producer, you’re bound to have great ideas…but how do you make them a reality in a country where you can’t speak the language? Partner with us!</p>
      <p>We are native English speakers so nothing gets lost in translation. We’ll catch hold of your vision, and with local know-how, we’ll make it happen.</p>
      <p class="strong">No job is too big, too small, too hard, too far away, or too urgent. Try us!</p>
      <ul class="benefits">
        <li><svg width="14" height="9" viewBox="0 0 14 9"><path d="M0 0l5 4.5L0 9M6 0l5 4.5L6 9" fill="none" stroke="#e8562a" stroke-width="2.2"/></svg>We provide camera crews and facilities throughout Germany and Europe</li>
        <li><svg width="14" height="9" viewBox="0 0 14 9"><path d="M0 0l5 4.5L0 9M6 0l5 4.5L6 9" fill="none" stroke="#e8562a" stroke-width="2.2"/></svg>We shoot in both PAL and NTSC</li>
        <li><svg width="14" height="9" viewBox="0 0 14 9"><path d="M0 0l5 4.5L0 9M6 0l5 4.5L6 9" fill="none" stroke="#e8562a" stroke-width="2.2"/></svg>We edit either in-studio or on the move and we transfer urgent footage via FTP or SNG</li>
        <li><svg width="14" height="9" viewBox="0 0 14 9"><path d="M0 0l5 4.5L0 9M6 0l5 4.5L6 9" fill="none" stroke="#e8562a" stroke-width="2.2"/></svg>We are on call 24/7</li>
      </ul>
    </div>

    <div class="tabs abs">
      <div class="tab contact">CONTACT US</div>
      <div class="tab guide">LOCATION GUIDE</div>
      <div class="tab testimonials">TESTIMONIALS</div>
    </div>
    <div class="testimonial-panel abs">
      <div class="quote-mark abs" style="left:12px;top:14px">“</div>
      <p class="quote-text abs">Lorem ipsum dolor sit amet, consectetur adipiscing elit. Vestibulum eget eros in augue vestibulum imperdiet a at leo. Sed elementum rutrum augue sit amet aliquam. Morbi metus leo, hendrerit at hendrerit nec, faucibus eget arcu.</p>
      <div class="quote-author abs">- dignissim egestas.</div>
      <div class="quote-mark abs" style="left:530px;top:12px">”</div>
    </div>
  </main>

  <aside>
    <div class="sidebar-rule abs"></div>
    <h2 class="news-heading abs">latest news</h2>
    <article class="post abs" style="top:504px">
      <h3 class="post-title abs">BLOG TITLE</h3>
      <div class="post-meta abs">ADDED BY <a>ANTON</a> IN <a>TECHNOLOGY</a> ON 25/12/2039</div>
      <p class="post-body abs">Lorem ipsum dolor sit amet, consectetur adipi-scing elit. Donec pellentesque viverra posuere. Ut aliquam suscipit commodo. Sed tristique cursus libero,</p>
      <div class="post-more abs">READ MORE <b>»</b></div>
      <div class="post-comments abs">▢ 12 COMMENTS</div>
    </article>
    <article class="post abs" style="top:715px">
      <h3 class="post-title abs">BLOG TITLE</h3>
      <div class="post-meta abs">ADDED BY <a>ANTON</a> IN <a>TECHNOLOGY</a> ON 25/12/2039</div>
      <p class="post-body abs">Lorem ipsum dolor sit amet, consectetur adipi-scing elit. Donec pellentesque viverra posuere. Ut aliquam suscipit commodo. Sed tristique cursus libero,</p>
      <div class="post-more abs">READ MORE <b>»</b></div>
      <div class="post-comments abs">▢ 12 COMMENTS</div>
    </article>
    <div class="share abs">Share with friends</div>
    <div class="blog-tab abs">VIEW OUR BLOG</div>
    <div class="share-dot abs" style="left:817px;background:#5a78b8"></div>
    <div class="share-dot abs" style="left:842px;background:#cfd6e8"></div>
    <div class="share-dot abs" style="left:867px;background:#5cb85c"></div>
    <div class="share-dot abs" style="left:892px;top:962px;background:#e8832a"></div>
    <div class="share-dot abs" style="left:917px;background:#6cbf73"></div>
  </aside>

  <footer class="site-footer abs">
    <div class="footer-col abs" style="left:46px">
      <h3>Site Pages</h3>
      <ul><li>About</li><li>Services</li><li>Recent Productions</li><li>Blog</li><li>Testimonials</li><li>Get a Quote</li><li>Contact</li><li>Film Library</li><li>Showreel</li><li>Events</li><li>Film Location Guide</li></ul>
    </div>
    <div class="footer-rule abs" style="left:178px"></div>
    <div class="footer-col abs" style="left:190px">
      <h3>Our Services</h3>
      <ul><li>Crews</li><li>Corporate Shoots</li><li>Webcasts</li><li>Production Arm</li><li>Legal Videography</li><li>Recent Productions</li></ul>
    </div>
    <div class="footer-rule abs" style="left:330px"></div>
    <div class="footer-col abs" style="left:343px">
      <h3>Film Locations</h3>
      <ul><li>Frankfurt</li><li>Cologne</li><li>Zurich</li><li>Helsinki</li><li>Amsterdam</li><li>London</li><li>Paris</li><li>Rome</li><li>Brussels</li><li>Berlin</li><li>Munich</li></ul>
    </div>
    <div class="footer-rule abs" style="left:480px"></div>
    <div class="footer-col abs" style="left:496px">
      <h3>Useful Links</h3>
      <ul><li>Link</li><li>Link 1</li><li>Link 2</li><li>Link 3</li><li>Link 4</li><li>Link 5</li></ul>
    </div>
    <div class="footer-rule abs" style="left:630px"></div>
    <div class="footer-about abs">
      <div class="copy">© 2010 lens harbor teutonia</div>
      <p>c/o Brightmoor Films • Lindenweg 12 • 60311<br>Frankfurt/Main • Germany<br>• info@lens-harbor-teutonia.com<br>Tel.: +49-69-417253<br>• Toll free from the USA 1-866-555-0142<br>Disclaimer</p>
    </div>
  </footer>

</div>
</body>
</html>
```